Business card for Chiropractic clinics needs reworked / redesigned

The business card in attachment was designed 10 years ago. It is in need of an update.
We have 2 clinics:
HALSPUNT VORDA & HALSPUNT MIRBE
Only one address needs to be on the card for doctors that only work in one clinic and two addresses need to be on the card for the doctors that work in both clinics.

Target Market(s)

patients/referrers

Industry/Entity Type

Medical

Contact Information for Business Card

Logo (in full or zoomed-in)
Clinic Name
Doctor name and title
clinic address, website, tel, email

Font styles to use
Sans Serif

Colors

Designer to choose colors to be used in the design.

Requirements
Must have
• Good contrast/readability
• We like modern minimalistic designs
• The Bcard needs to project our very high standard of proficiency/professionalism
Should not have
• Not curly
• Not to much colours

```html
<!DOCTYPE html>
<html lang="en">
<head>
<meta charset="utf-8">
<title>Halspunt Vorda – Business Card</title>
<link href="https://fonts.googleapis.com/css2?family=Figtree:wght@400;500;600&display=swap" rel="stylesheet">
<style>
  :root {
    --stage: #3b3b3b;
    --card-light: #ffffff;
    --ink: #03211f;
    --muted: #6e6e6e;
    --rule: #b8b8b8;
    --card-dark: #03211f;
    --on-dark: #ffffff;
  }
  * { box-sizing: border-box; margin: 0; padding: 0; }
  html, body {
    width: 1200px; height: 960px; overflow: hidden;
    background: var(--stage);
    font-family: "Figtree", Arial, sans-serif;
  }
  .card {
    position: absolute;
    left: 281px;
    width: 655px; height: 373px;
    border-radius: 22px;
    box-shadow: 0 6px 16px rgba(0,0,0,.35);
  }
  .card--front { top: 80px; background: var(--card-light); }
  .card--back { top: 506px; background: var(--card-dark); }

  .brand-mark {
    position: absolute;
    left: 142px; top: 132px; width: 150px;
    display: flex; flex-direction: column; align-items: center; gap: 16px;
    color: var(--ink);
    text-align: center;
  }
  .brand-mark__square { width: 40px; height: 40px; background: var(--ink); flex: none; }
  .brand-mark__name {
    font-size: 20px; font-weight: 600; letter-spacing: .03em; line-height: 25px;
  }

  .divider {
    position: absolute; left: 299px; top: 93px;
    width: 1px; height: 185px; background: var(--rule);
  }
  .contact { position: absolute; left: 328px; top: 95px; color: var(--ink); }
  .contact__name { font-size: 22px; font-weight: 600; line-height: 1; }
  .contact__title { font-size: 17px; color: var(--muted); margin-top: 7px; line-height: 1.1; }
  .contact__list { list-style: none; margin-top: 18px; }
  .contact__item {
    position: relative; padding-left: 22px;
    font-size: 15px; line-height: 22px; color: var(--muted);
  }
  .contact__item svg { position: absolute; left: 0; top: 5px; width: 12px; height: 12px; fill: var(--ink); }
  .contact__item--clinic { color: var(--ink); font-weight: 500; }
  .contact__item--address { margin-bottom: 14px; }

  .back-square {
    position: absolute; left: 152px; top: 158px;
    width: 58px; height: 58px; background: var(--on-dark);
  }
  .back-brand {
    position: absolute; left: 0; width: 100%; top: 158px;
    padding-left: 120px; text-align: center; color: var(--on-dark);
  }
  .back-brand__name { font-size: 25px; font-weight: 600; letter-spacing: .01em; line-height: 1; }
  .back-brand__web { font-size: 15px; margin-top: 6px; }
</style>
</head>
<body>
  <section class="card card--front">
    <div class="brand-mark">
      <span class="brand-mark__square"></span>
      <span class="brand-mark__name">HALSPUNT<br>VORDA</span>
    </div>
    <div class="divider"></div>
    <div class="contact">
      <h1 class="contact__name">Liam Verhoeven</h1>
      <p class="contact__title">President &amp; CEO</p>
      <ul class="contact__list">
        <li class="contact__item contact__item--clinic">
          <svg viewBox="0 0 12 12"><path d="M6 0a4 4 0 0 0-4 4c0 3 4 8 4 8s4-5 4-8a4 4 0 0 0-4-4zm0 5.5A1.5 1.5 0 1 1 6 2.5a1.5 1.5 0 0 1 0 3z"/></svg>
          HALSPUNT VORDA
        </li>
        <li class="contact__item contact__item--address">Lindenlaan 48</li>
        <li class="contact__item">
          <svg viewBox="0 0 12 12"><path d="M2.5 0.5l2 2.5-1.2 1.3c.7 1.6 1.8 2.7 3.4 3.4L8 6.5l2.5 2-1 2.5C5 10.8 1.2 7 1 2.5z"/></svg>
          +32 9 555 01 23
        </li>
        <li class="contact__item">
          <svg viewBox="0 0 12 12"><path d="M0 2.5h12v7H0zm1 .7v.4l5 3 5-3v-.4z"/></svg>
          info@halspuntvorda.be
        </li>
        <li class="contact__item">
          <svg viewBox="0 0 12 12"><circle cx="6" cy="6" r="5.2" fill="none" stroke="#03211f" stroke-width="1.2"/><path d="M.8 6h10.4M6 .8c-2.6 3-2.6 7.4 0 10.4M6 .8c2.6 3 2.6 7.4 0 10.4" fill="none" stroke="#03211f" stroke-width="1"/></svg>
          www.halspuntvorda.be
        </li>
      </ul>
    </div>
  </section>

  <section class="card card--back">
    <span class="back-square"></span>
    <div class="back-brand">
      <h2 class="back-brand__name">HALSPUNT VORDA</h2>
      <p class="back-brand__web">www.halspuntvorda.be</p>
    </div>
  </section>
</body>
</html>
```